Presentation Folder

Design presentation folder for professional law firm. Our law firm primarily represents individuals who are dealing with divorce, child custody, child support, spousal support, wills, estates and other civil litigation.
We desire a simple, professional, but memorable presentation folder that we can give clients containing their important documents (e.g., contract, and other important papers). The folder will also have a place for a business card. We will print this at Prindlebay. Specs and Templates are available at http://www.prindlebay-example.com/vp/ns/propath/UploadResources.aspx?selectedTab=0?pfid=156&pf_id=156&xnav=studio-side-bar#Templates
Our logo and one of our business cards is attached.
Our website is www.HolloweyFamilyLaw-example.com
Target Market(s)
Individual with legal issues primarily undergoing divorce
Industry/Entity Type
Law Firm
Font styles to use
Other font styles liked:
- Tahoma
Look and feel

```html
<!DOCTYPE html>
<html lang="en">
<head>
<meta charset="utf-8">
<title>Hollowey Law PLLC — Presentation Folder</title>
<link rel="stylesheet" href="https://fonts.googleapis.com/css2?family=Cinzel:wght@400;700&family=Libre+Baskerville:wght@400;700&display=swap">
<style>
  :root {
    --backdrop: #e9e6e1;
    --navy-light: #343b80;
    --navy: #262d68;
    --navy-deep: #1a1f4c;
    --band-blue: #3a4290;
    --band-blue-deep: #2e3580;
    --silver: #e4e5ee;
    --silver-dark: #a9abbb;
    --gold: #d8b85a;
    --gold-light: #f2e19a;
    --gold-deep: #b8912e;
    --cream: #f6eed2;
    --paper: #fbfbfb;
    --paper-shade: #ececec;
  }
  * { box-sizing: border-box; margin: 0; padding: 0; }
  html, body { width: 1200px; height: 800px; overflow: hidden; }
  body {
    background: var(--backdrop);
    position: relative;
    font-family: "Libre Baskerville", "Times New Roman", serif;
  }

  /* ---------- Front cover ---------- */
  .cover {
    position: absolute;
    left: 110px; top: 90px;
    width: 460px; height: 620px;
    background: radial-gradient(ellipse at 50% 45%, var(--navy-light) 0%, var(--navy) 55%, var(--navy-deep) 100%);
    box-shadow: 0 6px 18px rgba(0,0,0,.18);
    overflow: hidden;
  }
  .cover::after {
    content: "";
    position: absolute; left: 0; right: 0; bottom: 0; height: 6px;
    background: linear-gradient(90deg, var(--gold-deep), var(--gold-light), var(--gold-deep));
  }
  .title-band {
    position: absolute; left: 0; right: 0; top: 62px; height: 72px;
    background: linear-gradient(180deg, var(--band-blue) 0%, var(--band-blue-deep) 100%);
    border-top: 5px solid var(--silver);
    border-bottom: 5px solid var(--silver);
    display: flex; align-items: center; justify-content: center;
  }
  .firm-title {
    font-family: "Cinzel", "Times New Roman", serif;
    font-weight: 700;
    font-size: 33px;
    letter-spacing: 2px;
    color: var(--silver);
  }

  /* Framed name panel */
  .name-panel {
    position: absolute; left: 108px; top: 238px;
    width: 244px; height: 252px;
    padding: 7px;
    background: linear-gradient(180deg, #ffffff, var(--silver-dark));
    box-shadow: 0 3px 10px rgba(0,0,0,.35);
  }
  .name-panel .frame {
    width: 100%; height: 100%;
    padding: 9px;
    background: var(--navy-deep);
  }
  .name-panel .field {
    width: 100%; height: 100%;
    background: radial-gradient(ellipse at 50% 40%, var(--cream) 0%, var(--gold-light) 45%, var(--gold) 100%);
    display: flex; align-items: center; justify-content: center;
  }
  .name-panel .name {
    font-family: "Cinzel", "Times New Roman", serif;
    font-weight: 700;
    font-size: 28px;
    line-height: 1.3;
    text-align: center;
    letter-spacing: 2px;
    color: var(--navy);
  }

  .promise-band {
    position: absolute; left: 0; right: 0; top: 530px; height: 70px;
    background: linear-gradient(180deg, #232a62, #1d2352);
    border-top: 4px solid var(--silver);
    border-bottom: 4px solid var(--silver);
    display: flex; flex-direction: column; align-items: center; justify-content: center;
    gap: 8px;
  }
  .promise-band p {
    font-family: "Cinzel", "Times New Roman", serif;
    font-weight: 700;
    font-size: 12.5px;
    letter-spacing: 2.4px;
    color: var(--silver);
  }
  .promise-band .rule {
    width: 410px; height: 2px;
    background: var(--gold);
  }

  /* ---------- Inside right panel ---------- */
  .inside {
    position: absolute;
    left: 630px; top: 90px;
    width: 460px; height: 620px;
    background: linear-gradient(135deg, var(--paper) 0%, var(--paper-shade) 100%);
    box-shadow: 0 6px 18px rgba(0,0,0,.14);
    overflow: hidden;
  }
  .pocket {
    position: absolute; left: 0; right: 0; bottom: 0; height: 200px;
    background: linear-gradient(120deg, var(--gold-deep) 0%, var(--gold) 30%, var(--gold-light) 60%, var(--gold) 85%, var(--gold-deep) 100%);
    box-shadow: 0 -2px 6px rgba(0,0,0,.12);
  }
  .business-card {
    position: absolute; left: 175px; top: 18px;
    width: 112px; height: 168px;
    background: linear-gradient(180deg, var(--navy-light), var(--navy-deep));
    clip-path: polygon(14px 0, 98px 0, 112px 14px, 112px 154px, 98px 168px, 14px 168px, 0 154px, 0 14px);
    display: flex; flex-direction: column; align-items: center;
    padding: 16px 8px 0;
    color: var(--silver);
    text-align: center;
  }
  .business-card .card-name {
    font-family: "Cinzel", "Times New Roman", serif;
    font-weight: 700;
    font-size: 11px;
    line-height: 1.3;
    color: var(--gold);
    margin-bottom: 16px;
  }
  .business-card .person { font-size: 6.5px; font-weight: 700; letter-spacing: .5px; }
  .business-card .role { font-size: 5.5px; margin-bottom: 8px; }
  .business-card .line { font-size: 5.5px; line-height: 1.6; }
</style>
</head>
<body>

  <section class="cover">
    <header class="title-band">
      <h1 class="firm-title">HOLLOWEY LAW PLLC</h1>
    </header>

    <div class="name-panel">
      <div class="frame">
        <div class="field" role="img" aria-label="Gold panel where the firm's classical column illustration belongs">
          <span class="name">HOLLOWEY<br>LAW</span>
        </div>
      </div>
    </div>

    <footer class="promise-band">
      <p>WE PROVIDE PERSONALIZED LEGAL COUNSEL</p>
      <span class="rule"></span>
      <p>IN THE AREAS OF FAMILY AND EDUCATION LAW</p>
    </footer>
  </section>

  <section class="inside">
    <div class="pocket">
      <div class="business-card">
        <span class="card-name">HOLLOWEY<br>LAW</span>
        <span class="person">DANIEL REED CARTER</span>
        <span class="role">Managing Attorney</span>
        <span class="line">120 Ashford Lane, Suite 4</span>
        <span class="line">Brookvale, NC 27601</span>
        <span class="line">T 555.010.2244</span>
        <span class="line">mail@hollowey-example.com</span>
      </div>
    </div>
  </section>

</body>
</html>
```